Bref créative
Halden Byte Solutions - Stationery
Business Cards, Letter Head & Envelopes
Professional
Gordon Pelley
President
379 Cobble Lane Suite 4150
Millbrook, MA 01590
gpelley@halden-byte.com
www.halden-byte.com

```html
<!DOCTYPE html>
<html lang="en">
<head>
<meta charset="utf-8">
<title>Halden Byte Solutions – Business Cards</title>
<link rel="stylesheet" href="https://fonts.googleapis.com/css2?family=Open+Sans:wght@400;600;700&display=swap">
<style>
  :root {
    --bg: #ece9e4;
    --card: #ffffff;
    --brand-red: #b3321c;
    --brand-red-dark: #8e2312;
    --ink: #3d3d3d;
    --ink-soft: #5a5a5a;
    --stripe-grey: #4a4a4a;
    --rule: #c9c9c9;
  }
  * { box-sizing: border-box; margin: 0; padding: 0; }
  html, body {
    width: 1200px; height: 852px; overflow: hidden;
    background: var(--bg);
    font-family: "Open Sans", Arial, sans-serif;
    color: var(--ink);
  }
  .stage { position: relative; width: 1200px; height: 852px; }

  .card {
    position: absolute;
    width: 520px; height: 297px;
    background: var(--card);
    border-radius: 14px;
    overflow: hidden;
    box-shadow: 0 3px 10px rgba(0,0,0,.12);
  }
  .card--front { left: 70px; top: 150px; }
  .card--back  { left: 610px; top: 400px; }

  .card__swoosh { position: absolute; inset: 0; width: 100%; height: 100%; }

  .brand { position: absolute; }
  .brand__row { display: flex; align-items: center; gap: 8px; }
  .brand__square { width: 14px; height: 14px; background: var(--brand-red); flex: none; }
  .brand__name {
    font-size: 25px; font-weight: 600; color: var(--ink);
    letter-spacing: -0.3px; white-space: nowrap;
  }
  .brand--back .brand__name { font-size: 20px; }
  .brand__tagline {
    font-size: 11px; color: var(--ink-soft);
    margin-left: 22px; margin-top: 1px; white-space: nowrap;
  }

  .person { position: absolute; }
  .person__name { font-size: 14px; font-weight: 700; color: var(--brand-red); }
  .person__title { font-size: 10px; font-weight: 700; color: var(--ink); margin-top: 1px; }
  .person__address { font-size: 11px; color: var(--ink-soft); line-height: 1.45; margin-top: 14px; white-space: nowrap; }

  .divider { position: absolute; width: 1px; background: var(--rule); }

  .contacts { position: absolute; list-style: none; }
  .contacts li {
    display: flex; align-items: center; gap: 7px;
    font-size: 10.5px; color: var(--ink-soft);
    height: 17px; white-space: nowrap;
  }
  .contacts svg { width: 10px; height: 10px; flex: none; }
</style>
</head>
<body>
<main class="stage">

  <!-- Front card -->
  <section class="card card--front">
    <svg class="card__swoosh" viewBox="0 0 520 297" aria-hidden="true">
      <path d="M0 120 C30 190 80 250 150 297 L115 297 C60 255 20 200 0 150 Z" fill="var(--stripe-grey)"/>
      <path d="M0 150 C20 200 60 255 115 297 L0 297 Z" fill="var(--brand-red)"/>
    </svg>

    <div class="brand" style="left:58px; top:58px;">
      <div class="brand__row">
        <span class="brand__square"></span>
        <span class="brand__name">Halden Byte Solutions</span>
      </div>
      <div class="brand__tagline">Insight through Practice</div>
    </div>

    <div class="person" style="left:40px; top:146px; text-align:right; width:162px;">
      <div class="person__name">Gordon Pelley</div>
      <div class="person__title">President</div>
      <div class="person__address">379 Cobble Lane Suite 4150<br>Millbrook, MA 01590</div>
    </div>

    <div class="divider" style="left:214px; top:142px; height:92px;"></div>

    <ul class="contacts" style="left:226px; top:143px;">
      <li><svg viewBox="0 0 10 10"><path d="M2 1 L4 1 L4.6 3 L3.4 4 Q4.3 5.8 6 6.6 L7 5.4 L9 6 L9 8 Q5 9 1.5 4.5 Q1 2.5 2 1Z" fill="var(--brand-red)"/></svg>978-555-0142</li>
      <li><svg viewBox="0 0 10 10"><rect x="2.5" y="1" width="5" height="3" fill="var(--brand-red)"/><rect x="1" y="4" width="8" height="4" rx="1" fill="var(--brand-red)"/><rect x="2.5" y="7" width="5" height="2.5" fill="var(--brand-red-dark)"/></svg>978-555-0148</li>
      <li><svg viewBox="0 0 10 10"><circle cx="5" cy="5" r="4.5" fill="var(--brand-red)"/><rect x="2.6" y="3.4" width="4.8" height="3.4" fill="#fff"/><path d="M2.6 3.4 L5 5.3 L7.4 3.4" stroke="var(--brand-red)" stroke-width=".6" fill="none"/></svg>gpelley@halden-byte.com</li>
      <li><svg viewBox="0 0 10 10"><circle cx="5" cy="5" r="4.5" fill="var(--brand-red)"/><circle cx="5" cy="5" r="2.6" fill="none" stroke="#fff" stroke-width=".7"/><path d="M2.4 5 H7.6 M5 2.4 V7.6" stroke="#fff" stroke-width=".6"/></svg>www.halden-byte.com</li>
    </ul>
  </section>

  <!-- Back card -->
  <section class="card card--back">
    <svg class="card__swoosh" viewBox="0 0 520 297" aria-hidden="true">
      <path d="M520 70 C500 170 450 250 360 297 L400 297 C475 255 510 180 520 110 Z" fill="var(--stripe-grey)"/>
      <path d="M520 110 C510 180 475 255 400 297 L520 297 Z" fill="var(--brand-red)"/>
    </svg>

    <div class="person" style="left:290px; top:66px;">
      <div class="person__name">Gordon Pelley</div>
      <div class="person__title">President</div>
      <div class="person__address">379 Cobble Lane Suite 4150<br>Millbrook, MA 01590</div>
    </div>

    <div class="divider" style="left:276px; top:60px; height:190px;"></div>

    <div class="brand brand--back" style="left:28px; top:162px;">
      <div class="brand__row">
        <span class="brand__square"></span>
        <span class="brand__name">Halden Byte Solutions</span>
      </div>
      <div class="brand__tagline">Insight through Practice</div>
    </div>

    <ul class="contacts" style="left:290px; top:170px;">
      <li><svg viewBox="0 0 10 10"><path d="M2 1 L4 1 L4.6 3 L3.4 4 Q4.3 5.8 6 6.6 L7 5.4 L9 6 L9 8 Q5 9 1.5 4.5 Q1 2.5 2 1Z" fill="var(--brand-red)"/></svg>978-555-0142</li>
      <li><svg viewBox="0 0 10 10"><rect x="2.5" y="1" width="5" height="3" fill="var(--brand-red)"/><rect x="1" y="4" width="8" height="4" rx="1" fill="var(--brand-red)"/><rect x="2.5" y="7" width="5" height="2.5" fill="var(--brand-red-dark)"/></svg>978-555-0148</li>
      <li><svg viewBox="0 0 10 10"><circle cx="5" cy="5" r="4.5" fill="var(--brand-red)"/><rect x="2.6" y="3.4" width="4.8" height="3.4" fill="#fff"/><path d="M2.6 3.4 L5 5.3 L7.4 3.4" stroke="var(--brand-red)" stroke-width=".6" fill="none"/></svg>gpelley@halden-byte.com</li>
      <li><svg viewBox="0 0 10 10"><circle cx="5" cy="5" r="4.5" fill="var(--brand-red)"/><circle cx="5" cy="5" r="2.6" fill="none" stroke="#fff" stroke-width=".7"/><path d="M2.4 5 H7.6 M5 2.4 V7.6" stroke="#fff" stroke-width=".6"/></svg>www.halden-byte.com</li>
    </ul>
  </section>

</main>
</body>
</html>
```